Business Card Design

We need a business card designed to the point of print ready to take to our printers. the design should be professional, easy to read and simple. The cards should represent our business as professional and trust worthy.

Attached are several versions o the logo, and also the details for the card to be printed. please do communicate if different versions of the logo is required.

Business

```html
<!DOCTYPE html>
<html lang="en">
<head>
<meta charset="utf-8">
<title>PaySwift Recovery – Business Card</title>
<link rel="stylesheet" href="https://fonts.googleapis.com/css2?family=Exo+2:wght@600&family=Roboto+Slab:wght@400;700&display=swap">
<style>
  :root {
    --backdrop: #4a2f18;
    --card: #1b1b1b;
    --card-edge: #141414;
    --accent: #f0a01e;
    --logo-grey: #a9a9a9;
    --name-grey: #a5a5a5;
    --text-light: #d8d8d8;
    --web-white: #ffffff;
    --faint-line: #2c2c2c;
    --script-tone: #202020;
  }
  * { margin: 0; padding: 0; box-sizing: border-box; }
  html, body { width: 1200px; height: 900px; overflow: hidden; }
  body { background: var(--backdrop); position: relative; }

  .card {
    position: absolute;
    background: var(--card);
    border: 1px solid var(--card-edge);
    overflow: hidden;
  }
  .card--front { left: 71px; top: 72px; width: 585px; height: 363px; }
  .card--back  { left: 562px; top: 481px; width: 584px; height: 384px; }

  .wordmark {
    position: absolute;
    font-family: "Exo 2", sans-serif;
    font-weight: 600;
    color: var(--logo-grey);
    line-height: 1;
    text-align: right;
    white-space: nowrap;
  }
  .wordmark__name { display: block; letter-spacing: -0.5px; }
  .wordmark__suffix { display: block; margin-top: 4px; }
  .card--front .wordmark { left: 156px; top: 146px; }
  .card--front .wordmark__name { font-size: 34px; }
  .card--front .wordmark__suffix { font-size: 18px; }
  .card--back .wordmark { left: 44px; top: 74px; }
  .card--back .wordmark__name { font-size: 29px; }
  .card--back .wordmark__suffix { font-size: 16px; }

  .front__rule-h {
    position: absolute; left: 59px; top: 286px;
    width: 215px; height: 1px; background: var(--faint-line);
  }
  .front__rule-v {
    position: absolute; left: 553px; top: 18px;
    width: 1px; height: 262px; background: var(--faint-line);
  }
  .front__band {
    position: absolute; left: 0; top: 318px;
    width: 100%; height: 28px; background: var(--accent);
    display: flex; align-items: center; justify-content: center;
    font-family: "Roboto Slab", serif; font-weight: 700;
    font-size: 15px; color: var(--web-white);
  }

  .accent-bar { position: absolute; background: var(--accent); }
  .accent-bar--divider { left: 315px; top: 24px; width: 3px; height: 147px; }
  .accent-bar--right   { left: 576px; top: 32px; width: 8px; height: 169px; }
  .accent-bar--left    { left: 0; top: 186px; width: 8px; height: 198px; }

  .person { position: absolute; left: 41px; top: 246px; font-family: "Roboto Slab", serif; }
  .person__name { font-size: 25px; font-weight: 700; color: var(--name-grey); letter-spacing: 1.5px; word-spacing: 6px; }
  .person__role { font-size: 11.5px; font-weight: 700; color: var(--name-grey); letter-spacing: 0.8px; word-spacing: 3px; margin-top: 6px; }

  .contact { position: absolute; left: 360px; top: 206px; list-style: none; }
  .contact__item {
    display: flex; align-items: center; height: 40px; white-space: nowrap;
    font-family: "Roboto Slab", serif; font-size: 11.5px; color: var(--text-light);
  }
  .contact__icon { width: 18px; height: 18px; margin-right: 14px; flex: none; }

  .script-panel {
    position: absolute; left: 440px; top: 8px; width: 136px; height: 370px;
    background: linear-gradient(180deg, var(--script-tone), var(--card));
    opacity: 0.6;
  }
</style>
</head>
<body>

<section class="card card--front">
  <div class="wordmark">
    <span class="wordmark__name">PaySwift Recovery</span>
    <span class="wordmark__suffix">Pty Ltd</span>
  </div>
  <div class="front__rule-h"></div>
  <div class="front__rule-v"></div>
  <div class="front__band">www.payswiftrecovery.com.au</div>
</section>

<section class="card card--back">
  <div class="script-panel" role="img" aria-label="Faint handwritten script decoration"></div>
  <div class="wordmark">
    <span class="wordmark__name">PaySwift Recovery</span>
    <span class="wordmark__suffix">Pty Ltd</span>
  </div>
  <div class="accent-bar accent-bar--divider"></div>
  <div class="accent-bar accent-bar--right"></div>
  <div class="accent-bar accent-bar--left"></div>

  <div class="person">
    <div class="person__name">Danielle Harper</div>
    <div class="person__role">Managing Director</div>
  </div>

  <ul class="contact">
    <li class="contact__item">
      <svg class="contact__icon" viewBox="0 0 18 18" aria-hidden="true">
        <rect x="5" y="2" width="8" height="15" rx="1.5" fill="var(--accent)"/>
        <rect x="6.5" y="4" width="5" height="5" fill="var(--card)"/>
        <rect x="11" y="0" width="1.5" height="3" fill="var(--accent)"/>
      </svg>
      +61 400 555 018
    </li>
    <li class="contact__item">
      <svg class="contact__icon" viewBox="0 0 18 18" aria-hidden="true">
        <circle cx="9" cy="9" r="7.5" fill="var(--accent)"/>
        <g fill="none" stroke="var(--card)" stroke-width="1.1">
          <ellipse cx="9" cy="9" rx="3.2" ry="7.5"/>
          <line x1="1.5" y1="9" x2="16.5" y2="9"/>
          <line x1="3" y1="5" x2="15" y2="5"/>
          <line x1="3" y1="13" x2="15" y2="13"/>
        </g>
      </svg>
      www.payswiftrecovery.com.au
    </li>
    <li class="contact__item">
      <svg class="contact__icon" viewBox="0 0 18 18" aria-hidden="true">
        <rect x="1" y="4" width="16" height="11" rx="1" fill="var(--accent)"/>
        <rect x="1" y="7" width="16" height="2" fill="var(--card)"/>
      </svg>
      PO Box 1180 Harbour Qld 4000
    </li>
  </ul>
</section>

</body>
</html>
```